Training Certificate Design

Project: I will like to design a training certificate for our company with details below;

Company Logo

This is to Certify that
"Name of student"
Has completed the
VLMX Linking and Relaying v3.0 training
His practical work has been evaluated and demonstrated knowledge and experience.
on "Date"

Registration Number
58617092.4180526

Certificate Number
ZPHW8603152274

Signature space
Adetoro .F. Samuel
Chief Executive Officer

NOTE:

Find attached out company logo, our partner company logo, sample certificate and my signature.

```html
<!DOCTYPE html>
<html lang="en">
<head>
<meta charset="utf-8">
<title>Certificate of Appreciation</title>
<link rel="stylesheet" href="https://fonts.googleapis.com/css2?family=Playfair+Display:wght@700;800&family=Open+Sans:wght@400;600;700&family=Tinos:wght@400;700&display=swap">
<style>
  :root {
    --paper: #f4f4f5;
    --red: #e3262b;
    --red-dark: #b8181d;
    --grey-shape: #d9d9dc;
    --ink: #1d1d1f;
    --ink-soft: #333336;
    --rule: #2a2a2a;
    --partner: #3f5fa6;
  }
  * { box-sizing: border-box; margin: 0; padding: 0; }
  html, body { width: 851px; height: 1200px; overflow: hidden; background: #ffffff; }
  .certificate {
    position: relative;
    width: 851px;
    height: 1200px;
    background: var(--paper);
    overflow: hidden;
    color: var(--ink);
    font-family: "Open Sans", sans-serif;
  }
  .certificate__shapes { position: absolute; inset: 0; width: 851px; height: 1200px; }
  .brand {
    position: absolute; top: 40px; left: 0; width: 100%;
    display: flex; justify-content: center; align-items: center; gap: 10px;
  }
  .brand__mark { width: 22px; height: 22px; border-radius: 50%; background: var(--red); }
  .brand__name { font-family: "Open Sans", sans-serif; font-weight: 700; font-size: 26px; color: var(--ink); letter-spacing: 1px; }
  .title {
    position: absolute; top: 150px; left: 0; width: 100%;
    text-align: center;
    font-family: "Playfair Display", serif; font-weight: 800;
    font-size: 60px; line-height: 74px; letter-spacing: 2px; color: var(--ink);
  }
  .ribbon {
    position: absolute; top: 300px; left: 50%; transform: translateX(-50%);
    width: 450px; height: 46px;
    border: 2px solid var(--red-dark);
    background: #ffffff;
    display: flex; align-items: center; justify-content: center;
    font-family: "Tinos", serif; font-size: 26px; color: var(--ink);
  }
  .recipient-line {
    position: absolute; top: 428px; left: 175px; width: 515px;
    border-top: 2px solid var(--rule);
  }
  .course {
    position: absolute; top: 488px; left: 0; width: 100%; text-align: center;
  }
  .course__lead, .course__name { font-weight: 700; font-size: 31px; line-height: 42px; color: var(--ink); }
  .course__note {
    margin: 14px auto 0; width: 600px;
    font-family: "Tinos", serif; font-size: 23px; line-height: 30px; color: var(--ink-soft);
  }
  .date {
    position: absolute; top: 755px; left: 0; width: 100%; text-align: center;
    font-family: "Tinos", serif; font-weight: 700; font-size: 21px; color: var(--ink-soft);
  }
  .record {
    position: absolute; top: 865px;
    font-family: "Tinos", serif; font-size: 22px; line-height: 34px; color: var(--ink);
  }
  .record--registration { left: 58px; }
  .record--certificate { right: 58px; text-align: right; }
  .signatory { position: absolute; top: 940px; left: 0; width: 100%; text-align: center; }
  .signatory__signature {
    width: 190px; height: 70px; margin: 0 auto 8px;
    background: linear-gradient(90deg, #e6e6e8, #cfcfd3, #e6e6e8);
    border-radius: 4px;
  }
  .signatory__name, .signatory__role {
    font-family: "Tinos", serif; font-size: 22px; line-height: 30px; color: var(--ink);
  }
  .partner-badge {
    position: absolute; left: 25px; top: 1108px; width: 120px; height: 44px;
    border: 3px solid var(--partner); background: #ffffff;
  }
  .footer-brand {
    position: absolute; right: 40px; top: 1108px;
    font-family: "Open Sans", sans-serif; font-weight: 700; font-size: 40px; color: var(--ink);
  }
</style>
</head>
<body>
<main class="certificate">
  <svg class="certificate__shapes" viewBox="0 0 851 1200" aria-hidden="true">
    <polygon points="0,0 300,0 120,120 0,60" fill="var(--grey-shape)"/>
    <polygon points="0,0 230,0 0,150" fill="var(--red)"/>
    <polygon points="560,0 851,0 851,210" fill="var(--grey-shape)"/>
    <polygon points="640,0 851,0 851,150" fill="var(--red)"/>
    <polygon points="28,355 92,375 28,395" fill="var(--red)"/>
    <polygon points="0,368 40,375 0,382" fill="var(--red-dark)"/>
    <polygon points="823,730 760,752 823,772" fill="var(--red)"/>
    <polygon points="851,742 815,752 851,762" fill="var(--red-dark)"/>
    <polygon points="851,1010 851,1200 640,1200" fill="var(--grey-shape)"/>
    <polygon points="851,1070 851,1200 720,1200" fill="var(--red)"/>
  </svg>

  <header class="brand">
    <span class="brand__mark"></span>
    <span class="brand__name">Norvel ICT</span>
  </header>

  <h1 class="title">CERTIFICATE<br>OF APPERCIATION</h1>

  <div class="ribbon">This is to Proudly Certify that</div>

  <div class="recipient-line"></div>

  <section class="course">
    <p class="course__lead">Has completed the</p>
    <p class="course__name">VLMX Linking and Relaying v3.0 training</p>
    <p class="course__note">His practical work has been evaluated and demonstrated knowledge and experience.</p>
  </section>

  <p class="date">Date :</p>

  <div class="record record--registration">
    <p>Registration Number</p>
    <p>58617092.4180526</p>
  </div>
  <div class="record record--certificate">
    <p>Certificate Number</p>
    <p>ZPHW8603152274</p>
  </div>

  <section class="signatory">
    <div class="signatory__signature" role="img" aria-label="Handwritten signature of the Chief Executive Officer"></div>
    <p class="signatory__name">Adetoro .F. Samuel</p>
    <p class="signatory__role">Chief Executive Officer</p>
  </section>

  <div class="partner-badge" role="img" aria-label="Partner accreditation badge"></div>
  <div class="footer-brand">Quentara</div>
</main>
</body>
</html>
```